IT Company based on Biology Business Needs a Business Card Design

We need a business card design for a new company called 'Lumen CELL'. We develop the machine learning solutions especially focused on deep learning algorithms for biology industry. Our initial product is a vision detection on biological images to help doctors diagnose the symptoms. We would like to see designs that use the color green.

Industry/Entity Type

Business

```html
<!DOCTYPE html>
<html lang="en">
<head>
<meta charset="utf-8">
<title>Lumen CELL – Business Card</title>
<link href="https://fonts.googleapis.com/css2?family=Roboto:wght@400;700&display=swap" rel="stylesheet">
<style>
  :root {
    --page-bg: #b9bcbb;
    --sky-top: #a9cdea;
    --sky-mid: #eef5f4;
    --paper: #f7fbee;
    --meadow: #b6dc7e;
    --leaf-light: #9fd23c;
    --leaf-dark: #3f9a1d;
    --brand-green: #6cbb2d;
    --brand-deep: #11843a;
    --lime-light: #dce46e;
    --lime-dark: #bdd10a;
    --ink: #1a1a1a;
  }
  * { box-sizing: border-box; margin: 0; padding: 0; }
  html, body {
    width: 1200px; height: 1200px; overflow: hidden;
    background: var(--page-bg);
    font-family: "Roboto", Arial, sans-serif;
  }
  .card {
    position: absolute; left: 150px;
    width: 900px; height: 514px;
    overflow: hidden;
    box-shadow: 0 6px 18px rgba(0,0,0,.25);
  }
  .card--front {
    top: 50px;
    background: linear-gradient(180deg, var(--sky-top) 0%, var(--sky-mid) 45%, var(--paper) 85%, var(--meadow) 100%);
  }
  .card--back {
    top: 636px;
    background: linear-gradient(160deg, var(--lime-light) 0%, #d2de45 55%, var(--lime-dark) 100%);
  }
  .foliage {
    position: absolute;
    background: radial-gradient(ellipse at 70% 30%, var(--leaf-dark) 0%, var(--leaf-light) 55%, rgba(159,210,60,0) 72%);
  }
  .foliage--corner-right { right: -60px; top: -80px; width: 520px; height: 440px; }
  .foliage--corner-left { left: -40px; top: -40px; width: 170px; height: 180px; }
  .brand {
    position: absolute; display: flex; align-items: center;
    color: var(--brand-green); font-weight: 400; letter-spacing: -1px;
  }
  .brand__dot { border-radius: 50%; background: var(--brand-deep); flex: none; }
  .card--front .brand { left: 170px; top: 85px; font-size: 46px; gap: 14px; }
  .card--front .brand__dot { width: 26px; height: 26px; }
  .card--back .brand { left: 78px; top: 185px; font-size: 118px; gap: 30px; letter-spacing: -3px; }
  .card--back .brand__dot { width: 70px; height: 70px; }
  .holder {
    position: absolute; left: 0; width: 780px; top: 250px;
    text-align: center; color: var(--ink);
  }
  .holder__name { font-size: 31px; font-weight: 700; }
  .holder__title { font-size: 27px; margin-top: 10px; }
  .contact { position: absolute; top: 468px; font-size: 24px; color: var(--ink); }
  .contact--phone { left: 103px; }
  .contact--email { right: 100px; top: 460px; }
</style>
</head>
<body>
  <section class="card card--front">
    <div class="foliage foliage--corner-right" role="img" aria-label="Cluster of fresh green leaves"></div>
    <div class="foliage foliage--corner-left" role="img" aria-label="Small green leaves"></div>
    <div class="brand"><span class="brand__dot"></span>Lumen CELL</div>
    <div class="holder">
      <p class="holder__name">Mara Linden</p>
      <p class="holder__title">President, CEO</p>
    </div>
    <p class="contact contact--phone">555-014-2286</p>
    <p class="contact contact--email">mlinden@lumencell.net</p>
  </section>

  <section class="card card--back">
    <div class="brand"><span class="brand__dot"></span>Lumen CELL</div>
  </section>
</body>
</html>
```